Brindova Installation Van Project

wrap design for full size cargo van like torvel KX or vek haulwright. Use the logo and style guide as references. include some images of products as well as the elements indicated in our style guide . you can also reference our website

Target Market(s)

buyers of stairlifts or wheelchair ramps

Industry/Entity Type

access and mobility

Other font styles liked:
• Arial MT

Colors

Designer to choose colors to be used in the design.

Requirements
Must have
• our logo, meet our brand style guide. website URL

```html
<!DOCTYPE html>
<html lang="en">
<head>
<meta charset="utf-8">
<title>Brindova Installation Van Wrap</title>
<link rel="stylesheet" href="https://fonts.googleapis.com/css2?family=Barlow:wght@600&family=Montserrat:wght@700;800&display=swap">
<style>
  :root{
    --navy:#0a3d5e;
    --navy-soft:#13507a;
    --orange:#f05a26;
    --orange-soft:#f47f2a;
    --white:#ffffff;
    --photo-a:#d8d4cf;
    --photo-b:#8e8a86;
  }
  html,body{margin:0;padding:0;width:732px;height:1200px;overflow:hidden;background:var(--white);}
  .sheet{display:block;width:732px;height:1200px;}
  .wordmark{font-family:"Barlow",Arial,sans-serif;font-weight:600;}
  .wrap-text{font-family:"Montserrat",Arial,sans-serif;font-weight:800;}
  .fill-navy{fill:var(--navy);}
  .fill-navy-soft{fill:var(--navy-soft);}
  .fill-orange{fill:var(--orange);}
  .fill-orange-soft{fill:var(--orange-soft);}
  .fill-white{fill:var(--white);}
  .panel-frame{fill:none;stroke:#111;stroke-width:2;}
</style>
</head>
<body>
<svg class="sheet" viewBox="0 0 1512 2479" xmlns="http://www.w3.org/2000/svg">
  <defs>
    <clipPath id="clip-driver"><rect x="72" y="304" width="1387" height="518"/></clipPath>
    <clipPath id="clip-passenger"><rect x="44" y="883" width="1388" height="517"/></clipPath>
    <linearGradient id="photo-tone" x1="0" y1="0" x2="1" y2="1">
      <stop offset="0" stop-color="var(--photo-a)"/>
      <stop offset="1" stop-color="var(--photo-b)"/>
    </linearGradient>
  </defs>

  <!-- Brand name -->
  <text class="wordmark fill-navy" x="752" y="208" font-size="122" text-anchor="middle" letter-spacing="4">BRINDOVA</text>

  <!-- Driver side panel -->
  <g class="side-driver" clip-path="url(#clip-driver)">
    <g class="side-graphics">
      <rect class="fill-navy" x="72" y="304" width="1387" height="518"/>
      <polygon class="fill-white" points="72,620 1459,395 1459,822 72,822"/>
      <polygon class="fill-orange" points="72,757 1459,555 1459,822 72,822"/>
      <polygon class="fill-navy-soft" points="375,465 875,395 870,348 975,412 880,478 883,440 383,528"/>
      <polygon class="fill-orange-soft" points="552,785 640,690 640,740 1150,680 1150,735 650,800 650,830 610,830"/>
      <circle class="fill-orange" cx="1280" cy="520" r="198" stroke="var(--white)" stroke-width="26"/>
      <rect role="img" aria-label="Photo of two stairlift chairs with grey and taupe seats" x="1100" y="435" width="335" height="300" rx="24" fill="url(#photo-tone)"/>
    </g>
    <g transform="rotate(-9 840 480)">
      <rect class="fill-orange" x="600" y="450" width="480" height="62" rx="31"/>
      <circle class="fill-white" cx="636" cy="481" r="22"/>
      <path d="M628 471 q-4 10 6 20 q6 4 10 -1 l-4 -5 q-3 2 -6 -2 q-3 -4 0 -6 l-4 -6 z" class="fill-orange"/>
      <text class="wrap-text fill-white" x="670" y="500" font-size="46">(555) 014-2297</text>
    </g>
    <text class="wrap-text fill-navy" x="775" y="640" font-size="100" text-anchor="middle" transform="rotate(-9 775 610)">BRINDOVA</text>
    <text class="wrap-text fill-white" x="850" y="695" font-size="40" text-anchor="middle" transform="rotate(-9 850 680)">BRINDOVA.COM</text>
  </g>
  <rect class="panel-frame" x="72" y="304" width="1387" height="518"/>

  <!-- Passenger side panel -->
  <g class="side-passenger" clip-path="url(#clip-passenger)">
    <g transform="translate(1503,579) scale(-1,1)">
      <rect class="fill-navy" x="72" y="304" width="1387" height="518"/>
      <polygon class="fill-white" points="72,620 1459,395 1459,822 72,822"/>
      <polygon class="fill-orange" points="72,757 1459,555 1459,822 72,822"/>
      <polygon class="fill-navy-soft" points="375,465 875,395 870,348 975,412 880,478 883,440 383,528"/>
      <polygon class="fill-orange-soft" points="552,785 640,690 640,740 1150,680 1150,735 650,800 650,830 610,830"/>
      <circle class="fill-orange" cx="1280" cy="520" r="198" stroke="var(--white)" stroke-width="26"/>
    </g>
    <rect role="img" aria-label="Photo of two stairlift chairs with taupe and grey seats" x="68" y="1010" width="345" height="305" rx="24" fill="url(#photo-tone)"/>
    <g transform="rotate(8 670 1060)">
      <rect class="fill-orange" x="425" y="1028" width="480" height="62" rx="31"/>
      <circle class="fill-white" cx="461" cy="1059" r="22"/>
      <path d="M453 1049 q-4 10 6 20 q6 4 10 -1 l-4 -5 q-3 2 -6 -2 q-3 -4 0 -6 l-4 -6 z" class="fill-orange"/>
      <text class="wrap-text fill-white" x="495" y="1077" font-size="46">(555) 014-2297</text>
    </g>
    <text class="wrap-text fill-navy" x="728" y="1200" font-size="106" text-anchor="middle" transform="rotate(8 728 1170)">BRINDOVA</text>
    <text class="wrap-text fill-white" x="652" y="1272" font-size="40" text-anchor="middle" transform="rotate(8 652 1258)">BRINDOVA.COM</text>
  </g>

  <!-- Front view -->
  <g class="view-front">
    <rect class="fill-navy" x="207" y="1728" width="123" height="160"/>
    <rect class="fill-navy" x="557" y="1728" width="123" height="160"/>
    <polygon class="fill-orange" points="325,1728 337,1728 353,1888 341,1888"/>
    <polygon class="fill-orange" points="550,1728 562,1728 546,1888 534,1888"/>
    <text class="wordmark fill-navy" x="443" y="1822" font-size="32" text-anchor="middle">BRINDOVA</text>
  </g>

  <!-- Rear view -->
  <g class="view-rear">
    <rect class="fill-navy" x="868" y="1503" width="481" height="290"/>
    <rect class="fill-white" x="868" y="1793" width="481" height="169"/>
    <rect class="fill-orange" x="880" y="1789" width="458" height="12"/>
    <polygon class="fill-orange" points="1100,1775 1130,1795 1100,1815"/>
    <text class="wordmark fill-white" x="1106" y="1674" font-size="50" text-anchor="middle">BRINDOVA</text>
    <circle class="fill-white" cx="999" cy="1718" r="11"/>
    <text class="wrap-text fill-white" x="1120" y="1727" font-size="26" text-anchor="middle">(555) 014-2297</text>
    <text class="wrap-text fill-orange" x="1101" y="1751" font-size="18" text-anchor="middle">BRINDOVA.COM</text>
    <rect role="img" aria-label="Photo of a stairlift chair" x="1150" y="1764" width="135" height="160" rx="14" fill="url(#photo-tone)"/>
    <rect class="panel-frame" x="868" y="1503" width="481" height="459"/>
  </g>

  <!-- Roof stripes -->
  <g class="roof-stripes">
    <rect class="fill-navy" x="136" y="2017" width="1233" height="61"/>
    <rect class="fill-orange" x="136" y="2089" width="1233" height="13"/>
    <rect class="fill-orange" x="136" y="2337" width="1233" height="13"/>
    <rect class="fill-navy" x="136" y="2362" width="1233" height="62"/>
  </g>
</svg>
</body>
</html>
```